HARBORLINE AUTO GLASS

Mobile Glass Shop:

1) Windshield REPAIR 2)Windshield replacment 3) Rear Windshield Replacment 4) Side Window Replacment 5) car window replacment 6) Power Window Repair.

Schedual a service within 24 hour with one of our certified technicians.

See "brightvane auto repair" web site for referance on the nature of our buisness and service. www.brightvane-example.com

```html
<!DOCTYPE html>
<html lang="en">
<head>
<meta charset="utf-8">
<title>Harborline Auto Glass</title>
<link href="https://fonts.googleapis.com/css2?family=Roboto:wght@400;500;700&display=swap" rel="stylesheet">
<style>
:root{
  --navy:#0d65a3;
  --blue:#1a78bd;
  --sky:#1fa6f0;
  --cyan:#2ed3ff;
  --ink:#222;
  --muted:#444;
  --grey:#eeeeee;
  --footer:#3a3a3a;
  --footer-base:#2c2c2c;
  --white:#fff;
}
*{margin:0;padding:0;box-sizing:border-box}
html,body{width:1200px;height:3353px;overflow:hidden}
body{position:relative;font-family:'Roboto',sans-serif;color:var(--ink);background:var(--white)}
.abs{position:absolute}
a{color:inherit;text-decoration:none}

/* top bar */
.topbar{left:0;top:0;width:1200px;height:55px;background:var(--navy);color:var(--white);font-size:13px}
.topbar .follow{left:112px;top:20px}
.topbar .social{left:186px;top:19px;display:flex;gap:14px}
.social span{width:16px;height:16px;border-radius:50%;background:currentColor;display:block}
.topbar .phone{left:766px;top:19px;display:flex;gap:6px;align-items:center}
.topbar .mail{left:893px;top:19px;display:flex;gap:6px;align-items:center}

/* header */
.header{left:0;top:55px;width:1200px;height:127px;background:var(--white);box-shadow:0 2px 6px rgba(0,0,0,.12);z-index:2}
.brand{left:115px;top:42px;display:flex;align-items:center;gap:10px;color:var(--blue);font-weight:700;font-size:22px;letter-spacing:.5px}
.brand i{width:34px;height:34px;background:var(--blue);display:block}
.nav{top:56px;font-size:17px;color:var(--ink)}
.cta-head{left:876px;top:43px;width:212px;height:44px;background:var(--sky);border-radius:4px;color:var(--white);font-size:17px;font-weight:500;display:flex;align-items:center;justify-content:center;gap:8px}

/* hero */
.hero{left:0;top:182px;width:1200px;height:579px;overflow:hidden;background:#fff}
.hero-photo{left:430px;top:0;width:770px;height:579px;background:linear-gradient(90deg,#ffffff 0%,#c8ced6 30%,#8f98a4 60%,#5f6c7c 100%)}
.hero-title{left:138px;top:78px;font-size:42px;line-height:47px;color:var(--blue);font-weight:500}
.hero-text{left:138px;top:249px;width:450px;font-size:20px;line-height:27px;color:var(--ink)}
.btn{border-radius:4px;font-size:17px;display:flex;align-items:center;justify-content:center}
.btn-solid{background:var(--navy);color:var(--white)}
.btn-outline{border:1.5px solid var(--navy);color:var(--navy);font-weight:500;background:#fff}
.arrow-box{width:52px;height:54px;border:1px solid #ccc;display:flex;align-items:center;justify-content:center}
.hero-wave{left:0;top:500px}

/* intro */
.glass-img{left:117px;top:885px;width:436px;height:234px;background:linear-gradient(180deg,#e7eeed,#c9d6d4);border-radius:4px}
.intro-h{left:631px;top:842px;font-size:31px;line-height:35px;font-weight:500}
.intro-p{left:631px;top:922px;width:460px;font-size:16.5px;line-height:24.2px;color:var(--ink)}

/* how it works */
.sec-title{width:1200px;left:0;text-align:center;font-size:35px;font-weight:500}
.frame{width:264px;height:260px;border:4px solid var(--navy);border-radius:16px}
.frame.dashed{border-style:dashed}
.step{width:216px;height:215px;background:var(--navy);color:var(--white);text-align:center;padding:24px 16px 0;display:flex;flex-direction:column;align-items:center}
.step.light{background:#2a7ab8}
.step h3{font-size:20px;font-weight:500;margin-top:14px}
.step p{font-size:14.5px;line-height:17px;margin-top:4px}

/* services */
.services{left:0;top:1682px;width:1200px;height:715px;background:linear-gradient(100deg,var(--navy) 0%,#1579c0 45%,var(--sky) 100%)}
.services .sec-title{top:77px;color:#d6f1ff}
.card{width:315px;height:221px;color:var(--white);overflow:hidden}
.card .ph{position:absolute;inset:0}
.card h3{position:absolute;left:32px;top:96px;font-size:26px;line-height:32px;font-weight:500}
.card a{position:absolute;left:32px;font-size:16px}

/* why */
.why-col{width:280px;text-align:center;display:flex;flex-direction:column;align-items:center}
.why-col h3{font-size:20px;font-weight:500;margin-bottom:16px}
.why-col p{font-size:14.5px;line-height:17.5px;color:var(--ink);width:245px}

/* cta */
.cta-band{left:0;top:2880px;width:1200px;height:270px;background:var(--grey)}
.cta-band h2{position:absolute;left:0;width:1200px;text-align:center;top:65px;font-size:26px;font-weight:500}

/* footer */
.footer{left:0;top:3147px;width:1200px;height:178px;background:var(--footer);color:#e6e6e6}
.footer h4{font-size:13px;font-weight:500;margin-bottom:10px}
.footer li{list-style:none;font-size:11.5px;line-height:16.5px}
.fline{display:flex;align-items:center;gap:8px;font-size:11.5px;margin-bottom:8px}
.copy{left:0;top:3325px;width:1200px;height:28px;background:var(--footer-base);color:#999;font-size:10px;text-align:center;line-height:28px}
</style>
</head>
<body>

<div class="abs topbar">
  <span class="abs follow">Follow us</span>
  <div class="abs social"><span></span><span></span><span></span></div>
  <div class="abs phone">
    <svg width="18" height="18" viewBox="0 0 24 24" fill="none" stroke="#fff" stroke-width="1.8"><path d="M5 3h4l2 5-2.5 1.5a11 11 0 0 0 6 6L16 13l5 2v4a2 2 0 0 1-2 2A16 16 0 0 1 3 5a2 2 0 0 1 2-2z"/></svg>
    000 000 004
  </div>
  <div class="abs mail">
    <svg width="18" height="14" viewBox="0 0 24 18" fill="none" stroke="#fff" stroke-width="1.8"><rect x="1" y="1" width="22" height="16" rx="2"/><path d="M1 2l11 8 11-8"/></svg>
    info@harborlineautoglass.com
  </div>
</div>

<header class="abs header">
  <div class="abs brand"><i></i>HARBORLINE AUTO GLASS</div>
  <a class="abs nav" style="left:478px">Home</a>
  <a class="abs nav" style="left:557px">Services <svg width="10" height="8" viewBox="0 0 10 8"><path d="M1 2l4 4 4-4" fill="none" stroke="#222" stroke-width="1.3"/></svg></a>
  <a class="abs nav" style="left:648px">Covered Area</a>
  <a class="abs nav" style="left:775px">Contact</a>
  <a class="abs cta-head">
    <svg width="22" height="22" viewBox="0 0 24 24" fill="none" stroke="#fff" stroke-width="1.6"><rect x="3" y="5" width="18" height="16" rx="2"/><path d="M3 10h18M8 3v4M16 3v4M9 15l2 2 4-4"/></svg>
    GET APPOINTMENT
  </a>
</header>

<section class="abs hero">
  <div class="abs hero-photo" role="img" aria-label="Technician in cap and gloves fitting a new windscreen onto a car with suction lifters"></div>
  <h1 class="abs hero-title">Windscreen Replacement<br>&amp; Vehicle Glass Repair<br>Specialists</h1>
  <p class="abs hero-text">Our fully trained team of windscreen replacement &amp; repair experts are available 7 days a week, 365 days a year to give you all the help and advice you need</p>
  <a class="abs btn btn-solid" style="left:135px;top:400px;width:212px;height:44px">Schedulle online today!</a>
  <a class="abs btn btn-outline" style="left:371px;top:400px;width:155px;height:44px">OUR SERVICES</a>
  <div class="abs arrow-box" style="left:39px;top:235px"><svg width="20" height="16" viewBox="0 0 20 16"><path d="M19 8H2M8 2L2 8l6 6" fill="none" stroke="#bbb" stroke-width="1.5"/></svg></div>
  <div class="abs arrow-box" style="left:1102px;top:253px;border-color:#fff"><svg width="20" height="16" viewBox="0 0 20 16"><path d="M1 8h17M12 2l6 6-6 6" fill="none" stroke="#fff" stroke-width="1.5"/></svg></div>
  <svg class="abs hero-wave" width="1200" height="79" viewBox="0 0 1200 79" preserveAspectRatio="none">
    <defs><linearGradient id="hw" x1="0" x2="1"><stop offset="0" stop-color="#1a8fd6"/><stop offset="1" stop-color="#2ed3ff"/></linearGradient></defs>
    <path d="M0 8 C300 40 700 60 1200 40 L1200 79 L0 79Z" fill="url(#hw)"/>
    <path d="M0 60 L1200 66 L1200 79 L0 79Z" fill="#0d65a3"/>
  </svg>
</section>

<div class="abs glass-img" role="img" aria-label="Replacement car windscreen glass panel"></div>
<h2 class="abs intro-h">Need it fixing today?<br>No problem!</h2>
<p class="abs intro-p">Harborline Auto Glass is your one-stop platform for finding quality independent automotive glass technicians near you. Get in touch with over 300 experienced same-day and next-day windscreen repair and windscreen fitters today. All auto glaziers listed on Harborline Auto Glass must first undergo a thorough vetting process which verifies that they are committed to quality and to customer service. If you've been searching online for 'windscreen repair near me', you've come to the right place. Give Harborline Auto Glass a go today and save time and money.</p>

<h2 class="abs sec-title" style="top:1235px;color:#333">How it works</h2>
<div class="abs frame dashed" style="left:163px;top:1334px"></div>
<div class="abs frame" style="left:469px;top:1334px"></div>
<div class="abs frame dashed" style="left:773px;top:1334px"></div>
<svg class="abs" style="left:425px;top:1455px" width="50" height="24"><path d="M0 12h38" stroke="#0d65a3" stroke-width="4"/><path d="M36 4l12 8-12 8z" fill="#0d65a3"/></svg>
<svg class="abs" style="left:729px;top:1455px" width="50" height="24"><path d="M0 12h38" stroke="#0d65a3" stroke-width="4"/><path d="M36 4l12 8-12 8z" fill="#0d65a3"/></svg>

<div class="abs step" style="left:187px;top:1360px">
  <svg width="60" height="62" viewBox="0 0 60 62" fill="none" stroke="#fff" stroke-width="2"><rect x="6" y="6" width="38" height="50"/><path d="M13 18h24M13 26h24M13 34h18M13 42h14"/><path d="M52 20L36 48l-4 4 1-6 16-28z"/></svg>
  <h3>1. Get a quote</h3>
  <p>Tell us about your car repair needs and get a quote</p>
</div>
<div class="abs step light" style="left:491px;top:1360px">
  <svg width="66" height="66" viewBox="0 0 66 66" fill="none" stroke="#fff" stroke-width="2"><rect x="14" y="4" width="38" height="22" rx="2"/><path d="M8 28h50v22H8z"/><path d="M16 46l4-10h26l4 10M12 46h42v8H12z"/><circle cx="20" cy="56" r="4"/><circle cx="46" cy="56" r="4"/></svg>
  <h3>2. Make a booking</h3>
  <p>Approve the quote to make a booking for collection and delivery</p>
</div>
<div class="abs step" style="left:796px;top:1356px">
  <svg width="62" height="66" viewBox="0 0 62 66" fill="none" stroke="#fff" stroke-width="2"><path d="M10 8l6 6-4 4-6-6a8 8 0 0 0 10 10l8 8"/><rect x="14" y="40" width="34" height="22" rx="3"/><path d="M31 40v22M20 30h22v10H20z"/><path d="M22 30a9 9 0 0 1 18 0"/></svg>
  <h3>3. We Repair</h3>
  <p>Get your car fixed and delivered back to you, all from home</p>
</div>

<section class="abs services">
  <h2 class="abs sec-title">Our Services</h2>
  <div class="abs card" style="left:115px;top:160px"><div class="ph" role="img" aria-label="Two technicians lifting a windshield onto a car" style="background:linear-gradient(135deg,#8a8f98,#3c4450 55%,#6f89a4)"></div><h3>Windshield<br>Repair</h3><a style="top:170px">Learn more →</a></div>
  <div class="abs card" style="left:443px;top:160px"><div class="ph" role="img" aria-label="Shattered windshield glass" style="background:linear-gradient(135deg,#6e7276,#2e3236 60%,#55595e)"></div><h3>Windshield<br>Replacement</h3><a style="top:175px">Learn more →</a></div>
  <div class="abs card" style="left:769px;top:160px"><div class="ph" role="img" aria-label="Technician fitting a rear windshield" style="background:linear-gradient(135deg,#4a5058,#2a2e33 55%,#7a8088)"></div><h3>Rear Windshield<br>Replacment</h3><a style="top:180px">Learn more →</a></div>
  <div class="abs card" style="left:115px;top:400px"><div class="ph" role="img" aria-label="Rain on a car side window" style="background:linear-gradient(135deg,#5a7c9c,#1b2f4a 55%,#3d5f86)"></div><h3>Side Window<br>Replacment</h3><a style="top:180px">Learn more →</a></div>
  <div class="abs card" style="left:443px;top:400px"><div class="ph" role="img" aria-label="Technicians working on a car window in a workshop" style="background:linear-gradient(135deg,#8b939b,#3a4048 55%,#5e6872)"></div><h3>Car window<br>replacment</h3><a style="top:180px">Learn more →</a></div>
  <div class="abs card" style="left:769px;top:400px"><div class="ph" role="img" aria-label="Gloved hands repairing a power window mechanism" style="background:linear-gradient(135deg,#9aa0a6,#43484e 55%,#23272b)"></div><h3>Power Window<br>Repair</h3><a style="top:180px">Learn more →</a></div>
</section>

<h2 class="abs sec-title" style="top:2480px;color:#333">Why Choose Us</h2>
<div class="abs why-col" style="left:127px;top:2564px">
  <svg width="82" height="82" viewBox="0 0 82 82" fill="none" stroke="#0d65a3" stroke-width="2.5"><circle cx="52" cy="28" r="22"/><path d="M58 18h-9a5 5 0 0 0 0 10h6a5 5 0 0 1 0 10h-10M52 12v6M52 38v6"/><rect x="4" y="52" width="10" height="26"/><path d="M14 56l10-10 4-10h4v16h14a4 4 0 0 1 0 8v14H14"/></svg>
  <h3 style="margin-top:12px">Fair, transparent pricing</h3>
  <p>Harborline auto glass lets you request multiple quotes from nearby auto glaziers, completely for free and without any obligation to follow up.</p>
</div>
<div class="abs why-col" style="left:463px;top:2584px">
  <svg width="78" height="56" viewBox="0 0 78 56" fill="none" stroke="#0d65a3" stroke-width="2.5"><path d="M16 6h46l8 18v20H8V24z"/><path d="M14 24h50"/><rect x="8" y="44" width="10" height="8"/><rect x="60" y="44" width="10" height="8"/><path d="M14 34h8M56 34h8M30 36h18"/></svg>
  <h3 style="margin-top:16px">Convenience</h3>
  <p>With pick up &amp; delivery, our hassle-free process makes car maintance much more convenient for you.</p>
</div>
<div class="abs why-col" style="left:800px;top:2584px">
  <svg width="56" height="64" viewBox="0 0 56 64" fill="none" stroke="#0d65a3" stroke-width="3"><path d="M28 3l23 9v18c0 15-10 26-23 31C15 56 5 45 5 30V12z"/><path d="M17 32l8 8 15-16"/></svg>
  <h3 style="margin-top:22px">Professional and reliable</h3>
  <p>Professionals dedicated to quality services. Our membershave many years of experience,hold technical certificates and comply with all industry standards.</p>
</div>

<section class="abs cta-band">
  <h2>Schedual a service within 24 hour with one of our certified technicians</h2>
  <a class="abs btn btn-solid" style="left:495px;top:122px;width:210px;height:48px">Schedulle online today!</a>
</section>
<svg class="abs" style="left:0;top:3072px" width="1200" height="76" viewBox="0 0 1200 76" preserveAspectRatio="none">
  <defs><linearGradient id="cw" x1="0" x2="1"><stop offset="0" stop-color="#1a8fd6"/><stop offset="1" stop-color="#2ed3ff"/></linearGradient></defs>
  <path d="M0 58 C400 40 800 20 1200 0 L1200 76 L0 76Z" fill="url(#cw)"/>
  <path d="M0 66 L1200 60 L1200 76 L0 76Z" fill="#0d65a3"/>
</svg>

<footer class="abs footer">
  <div class="abs" style="left:145px;top:43px"><h4>Quick links</h4><ul><li>Home</li><li>Services</li><li>Covered area</li><li>Contact</li></ul></div>
  <div class="abs" style="left:298px;top:43px"><h4>Services</h4><ul><li>Windshield Repair</li><li>Windshield replacment</li><li>Rear Windshield Replacment</li><li>Side Window Replacment</li><li>Car window replacment</li><li>Power Window Repair</li></ul></div>
  <div class="abs" style="left:590px;top:46px"><h4 style="margin-bottom:18px">Business Information</h4>
    <div class="fline"><svg width="12" height="14" viewBox="0 0 12 14" fill="none" stroke="#ddd" stroke-width="1.2"><path d="M6 13s5-5 5-8A5 5 0 0 0 1 5c0 3 5 8 5 8z"/><circle cx="6" cy="5" r="1.8"/></svg>Your office location here,</div>
    <div class="fline"><svg width="13" height="13" viewBox="0 0 24 24" fill="none" stroke="#ddd" stroke-width="2"><path d="M5 3h4l2 5-2.5 1.5a11 11 0 0 0 6 6L16 13l5 2v4a2 2 0 0 1-2 2A16 16 0 0 1 3 5a2 2 0 0 1 2-2z"/></svg>000 000 004</div>
    <div class="fline"><svg width="13" height="10" viewBox="0 0 24 18" fill="none" stroke="#ddd" stroke-width="2"><rect x="1" y="1" width="22" height="16" rx="2"/><path d="M1 2l11 8 11-8"/></svg>info@harborlineautoglass.com</div>
  </div>
  <div class="abs" style="left:950px;top:51px"><ul><li style="line-height:20px">Privacy Policy</li><li style="line-height:20px">Term of use</li><li style="line-height:20px">Cancellation policy</li></ul>
    <div class="social" style="display:flex;gap:14px;margin-top:16px;color:#fff"><span></span><span></span><span></span></div>
  </div>
</footer>
<div class="abs copy">© 2022 Harborline Auto Glass</div>

</body>
</html>
```